Humorous Book by Comedian Needs E-book Cover

My book 'A Kettle on the Porch' is on Leafpad but I want a better cover designed. Cover needs my photo on it. My name is the most important text (because I have an existing audience.)

Text elements:
Author: Dorvel Pim
Title: A Kettle on the Porch
Subtitle: Tenth Anniversary Edition
Review Quote: 'All of his columns are amusing. The best are masterpieces.' Harbour Ledger

Above my name it should say: Collected Humour From NZ's Award-Winning Comedian

Here's the present version (which is why I want an improved version!)
http://www.brightmart-example.com/A-Kettle-Porch-Anniversary-Edition-ebook/dp/Q77TX2M904

Book covers I admire:

http://www.brightmart-example.co.uk/Why-The-Fern-Odile-Brask-ebook/dp/Q3318ZR7LN/ref=tmm_kin_title_0

http://www.brightmart-example.com/Gravelhat-Mira-Dunst-ebook/dp/Q691PLE583/ref=tmm_kin_title_0

http://www.brightmart-example.co.uk/Why-Keep-Lantern-Rex-Palfrey-ebook/dp/Q58JN3TQ7V

Leafpad covers need to work as thumbnails, as well as on small device screens.

This cover is for Brightmart Leafpad. Tech specs are on Leafpad Direct Publishing page. Dimensions: Requirements for the size of your cover art have an ideal height/width ratio of 1.6, this means: • A minimum of 625 pixels on the shortest side and 1000 pixels on the longest side • For best quality, your image would be 2820 pixels on the shortest side and 4500 pixels on the longest side

Dimensions Requirements for the size of your cover art have an ideal height/width ratio of 1.6, this means: • A minimum of 625 pixels on the shortest side and 1000 pixels on the longest side • For best quality, your image would be 2820 pixels on the shortest side and 4500 pixels on the longest side

Comedian

```html
<!DOCTYPE html>
<html lang="en">
<head>
<meta charset="utf-8">
<title>Dorvel Pim – A Kettle on the Porch</title>
<link rel="stylesheet" href="https://fonts.googleapis.com/css2?family=Tenor+Sans&family=Cinzel:wght@400;500&family=Archivo:wght@400;700&display=swap">
<style>
  :root {
    --page: #ffffff;
    --bg-dark: #474747;
    --bg-mid: #6f6f6f;
    --bg-light: #9c9c9c;
    --tagline: #f2b705;
    --name-light: #ffffff;
    --name-dark: #000000;
    --band-dark: #2e0000;
    --band-light: #5c0b0b;
    --edition-accent: #ff4a17;
    --portrait-light: #efe7cf;
    --portrait-dark: #b9ad8c;
  }
  html, body {
    margin: 0;
    padding: 0;
    width: 764px;
    height: 1200px;
    overflow: hidden;
    background: var(--page);
  }
  .cover {
    position: relative;
    width: 764px;
    height: 1200px;
    background: var(--page);
    overflow: hidden;
  }
  .cover-panel {
    position: absolute;
    left: 22px;
    top: 28px;
    width: 720px;
    height: 1147px;
    background: radial-gradient(ellipse 70% 45% at 58% 58%, var(--bg-light) 0%, var(--bg-mid) 55%, var(--bg-dark) 100%);
    overflow: hidden;
  }
  .tagline {
    position: absolute;
    left: 33px;
    top: 44px;
    margin: 0;
    font-family: "Archivo", Arial, sans-serif;
    font-size: 25px;
    letter-spacing: 0.2px;
    color: var(--tagline);
    white-space: nowrap;
  }
  .author {
    position: absolute;
    left: 0;
    top: 0;
    width: 720px;
    height: 560px;
    margin: 0;
  }
  .author text {
    font-family: "Tenor Sans", "Optima", sans-serif;
    font-weight: 400;
  }
  .author-first { fill: var(--name-light); font-size: 172px; }
  .author-last { fill: var(--name-dark); font-size: 358px; }
  .portrait {
    position: absolute;
    left: 0;
    top: 0;
    width: 720px;
    height: 1147px;
  }
  .title {
    position: absolute;
    right: 24px;
    top: 522px;
    margin: 0;
    font-family: "Cinzel", "Trajan Pro", serif;
    font-weight: 500;
    text-align: right;
    line-height: 1.5;
  }
  .title-line { display: block; font-size: 56px; white-space: nowrap; }
  .title-line--dark { color: var(--name-dark); }
  .title-line--light { color: var(--name-light); }
  .edition-band {
    position: absolute;
    left: 363px;
    top: 732px;
    width: 357px;
    height: 137px;
    background: linear-gradient(90deg, var(--band-dark), var(--band-light));
    font-family: "Tenor Sans", "Optima", sans-serif;
    color: var(--name-light);
    font-size: 45px;
    line-height: 45px;
  }
  .edition-band span { position: absolute; white-space: nowrap; }
  .edition-accent { color: var(--edition-accent); left: 62px; top: 8px; }
  .edition-word-2 { left: 43px; top: 49px; }
  .edition-word-3 { left: 125px; top: 88px; }
  .review {
    position: absolute;
    left: 0;
    top: 895px;
    width: 700px;
    margin: 0;
    font-family: "Tenor Sans", "Optima", sans-serif;
    color: var(--name-light);
    font-size: 36px;
    line-height: 37px;
  }
  .review-line { display: block; white-space: nowrap; }
  .review-line--1 { padding-left: 451px; }
  .review-line--2 { padding-left: 476px; }
  .review-line--3 { padding-left: 489px; }
  .review-line--4 { padding-left: 475px; }
  .review-line--5 { padding-left: 441px; }
  .review-source {
    position: absolute;
    right: 26px;
    top: 1090px;
    margin: 0;
    font-family: "Archivo", Arial, sans-serif;
    font-weight: 700;
    font-size: 22px;
    color: var(--name-light);
    white-space: nowrap;
  }
</style>
</head>
<body>
<main class="cover">
  <div class="cover-panel">
    <p class="tagline">Collected Humour From&nbsp; NZ's Award-Winning Comedian</p>
    <h1 class="author">
      <svg width="720" height="560" viewBox="0 0 720 560">
        <text class="author-first" x="33" y="227" textLength="663" lengthAdjust="spacingAndGlyphs">DORVEL</text>
        <text class="author-last" x="30" y="502" textLength="666" lengthAdjust="spacingAndGlyphs">PIM</text>
      </svg>
    </h1>
    <svg class="portrait" viewBox="0 0 720 1147" role="img" aria-label="Photo of the author smiling, in glasses, a cream dinner jacket and a dark bow tie">
      <defs>
        <linearGradient id="portraitTone" x1="0" y1="0" x2="1" y2="1">
          <stop offset="0" stop-color="var(--portrait-light)"/>
          <stop offset="1" stop-color="var(--portrait-dark)"/>
        </linearGradient>
      </defs>
      <path d="M75 470 Q72 412 170 410 Q268 410 276 470 Q284 560 248 620 L282 640 Q345 690 358 740 L360 870 Q420 905 432 960 Q432 1020 378 1050 L362 1147 L0 1147 L0 690 Q60 660 100 640 Q76 560 75 470 Z" fill="url(#portraitTone)"/>
    </svg>
    <h2 class="title">
      <span class="title-line title-line--dark">A Kettle on</span>
      <span class="title-line title-line--light">the Porch</span>
    </h2>
    <div class="edition-band">
      <span class="edition-accent">Tenth</span>
      <span class="edition-word-2">Anniversary</span>
      <span class="edition-word-3">Edition</span>
    </div>
    <blockquote class="review">
      <span class="review-line review-line--1">'All of his</span>
      <span class="review-line review-line--2">columns are</span>
      <span class="review-line review-line--3">amusing.</span>
      <span class="review-line review-line--4">The best are</span>
      <span class="review-line review-line--5">masterpieces.'</span>
    </blockquote>
    <p class="review-source">-Harbour Ledger</p>
  </div>
</main>
</body>
</html>
```